Morrow Realty Marketing Brochure

We are looking for a refresh/modern design to use on our marketing brochures...the blue paint brush stroke takes up a lot of space and isn't really speaking to us. Most of the material does not need to be reproduced...we are just looking for a clean template that we can use on all of our brochure pages, and then would like help on page 11 to make these pages look more professional.
Target Market(s)
Real Estate Developers, Small Businesses looking to lease space
Industry/Entity Type
Real Estate Development
Requirements
Nice to have
- Colors complementing the Morrow Logo

```html
<!DOCTYPE html>
<html lang="en">
<head>
<meta charset="UTF-8">
<title>Morrow Partners – Brochure Cover</title>
<link rel="stylesheet" href="https://fonts.googleapis.com/css2?family=Lato:wght@400;700&display=swap">
<style>
  :root {
    --navy: #1b2f66;
    --band-deep: #0c3a78;
    --band-light: #1f5aa3;
    --stripe: #0f2a5c;
    --paper: #ffffff;
    --sketch: #eef0f3;
    --ink: #222222;
    --accent-square: #2a64ad;
  }
  * { margin: 0; padding: 0; box-sizing: border-box; }
  html, body {
    width: 1200px;
    height: 900px;
    overflow: hidden;
    background: var(--paper);
    font-family: "Lato", sans-serif;
  }
  .cover {
    position: relative;
    width: 1200px;
    height: 900px;
    background: var(--paper);
  }
  .cover__backdrop {
    position: absolute;
    left: 0; top: 0;
    width: 1200px;
    height: 524px;
    background:
      linear-gradient(180deg, rgba(255,255,255,0) 0%, rgba(255,255,255,0.6) 100%),
      radial-gradient(ellipse at 10% 20%, var(--sketch) 0%, rgba(238,240,243,0) 45%),
      radial-gradient(ellipse at 92% 35%, var(--sketch) 0%, rgba(238,240,243,0) 45%);
  }
  .brand {
    position: absolute;
    top: 84px;
    left: 0;
    width: 1200px;
    display: flex;
    justify-content: center;
    align-items: center;
    gap: 18px;
  }
  .brand__square {
    width: 40px;
    height: 40px;
    background: var(--accent-square);
  }
  .brand__name {
    font-weight: 700;
    font-size: 46px;
    letter-spacing: 1px;
    color: var(--navy);
    line-height: 1;
  }
  .band {
    position: absolute;
    left: 0;
    top: 524px;
    width: 1200px;
    height: 293px;
    background: radial-gradient(ellipse at 50% 60%, var(--band-light) 0%, var(--band-deep) 75%);
  }
  .band__stripe {
    position: absolute;
    left: 0;
    top: 817px;
    width: 1200px;
    height: 10px;
    background: var(--stripe);
  }
  .hero-photo {
    position: absolute;
    left: 129px;
    top: 201px;
    width: 963px;
    height: 476px;
    border: 4px solid var(--paper);
    box-shadow: 0 6px 14px rgba(0,0,0,0.35);
    background:
      linear-gradient(180deg, #8fc1ea 0%, #c9e1f3 38%, #d9d6cd 62%, #9aa3a6 85%, #7b8a6a 100%);
  }
  .tagline {
    position: absolute;
    top: 722px;
    left: 0;
    width: 1200px;
    text-align: center;
    color: var(--paper);
    font-size: 38px;
    font-weight: 400;
    letter-spacing: 0.5px;
    line-height: 1.2;
    white-space: nowrap;
  }
  .tagline strong { font-weight: 700; }
  .footer {
    position: absolute;
    top: 827px;
    left: 0;
    width: 1200px;
    height: 73px;
    display: flex;
    align-items: center;
    justify-content: center;
  }
  .footer__url {
    font-size: 22px;
    letter-spacing: 3px;
    color: var(--ink);
  }
</style>
</head>
<body>
  <main class="cover">
    <div class="cover__backdrop" role="img" aria-label="Faint architectural line sketch of tall buildings"></div>

    <header class="brand">
      <span class="brand__square"></span>
      <span class="brand__name">MORROW PARTNERS</span>
    </header>

    <div class="band"></div>
    <div class="band__stripe"></div>

    <div class="hero-photo" role="img" aria-label="Photograph of a modern glass and stone office building under a blue sky with trees"></div>

    <h1 class="tagline"><strong>REAL ESTATE</strong> DEVELOPMENT COMPANY</h1>

    <footer class="footer">
      <span class="footer__url">www.morrowpartners.com</span>
    </footer>
  </main>
</body>
</html>
```